LVNODE
biz card
LVNODE - Information Technology
Creative Brief
Professional
jun pa
238 Elmora Pl, 3FL NewYorkCity, NY 10583
jun.pa@lanviretnode.com
www.lanviretnode.com

```html
<!DOCTYPE html>
<html lang="en">
<head>
<meta charset="utf-8">
<title>LVNODE business card</title>
<link href="https://fonts.googleapis.com/css2?family=Arimo:wght@400;700&display=swap" rel="stylesheet">
<style>
  :root {
    --backdrop: #6a2b18;
    --card: #ffffff;
    --ink: #3a3a3a;
    --accent: #e3202a;
  }
  html, body {
    margin: 0;
    width: 1200px;
    height: 965px;
    overflow: hidden;
    background: var(--backdrop);
  }
  .card {
    position: absolute;
    left: 80px;
    top: 188px;
    width: 1040px;
    height: 588px;
    background: var(--card);
    border-radius: 35px;
    box-shadow: 0 14px 30px rgba(0,0,0,0.35);
    font-family: "Arimo", Arial, sans-serif;
    color: var(--ink);
  }
  .name-tab {
    position: absolute;
    left: 0;
    top: 91px;
    width: 31px;
    height: 60px;
    background: var(--accent);
  }
  .name {
    position: absolute;
    left: 42px;
    top: 94px;
    margin: 0;
    font-size: 42px;
    font-weight: 700;
    line-height: 52px;
    color: var(--accent);
  }
  .address {
    position: absolute;
    left: 49px;
    top: 214px;
    margin: 0;
    font-size: 32px;
    line-height: 42px;
    font-style: normal;
  }
  .contacts {
    position: absolute;
    left: 56px;
    top: 322px;
    margin: 0;
    padding: 0;
    list-style: none;
    font-size: 31px;
    line-height: 43px;
  }
  .contacts li {
    display: flex;
    align-items: center;
    height: 43px;
  }
  .contacts svg {
    width: 26px;
    height: 26px;
    margin-right: 19px;
    fill: var(--accent);
  }
  .brand {
    position: absolute;
    left: 640px;
    top: 300px;
    width: 340px;
    text-align: center;
    font-size: 64px;
    font-weight: 700;
    letter-spacing: 2px;
    color: var(--accent);
  }
</style>
</head>
<body>
  <div class="card">
    <div class="name-tab"></div>
    <h1 class="name">jun pa</h1>
    <address class="address">238 Elmora Pl, 3FL<br>NewYorkCity,&nbsp; NY 10583</address>
    <ul class="contacts">
      <li>
        <svg viewBox="0 0 24 24" aria-hidden="true"><path d="M6.6 10.8a15 15 0 0 0 6.6 6.6l2.2-2.2c.3-.3.7-.4 1-.2 1.1.4 2.3.6 3.6.6.6 0 1 .4 1 1V20c0 .6-.4 1-1 1A17 17 0 0 1 3 4c0-.6.4-1 1-1h3.5c.6 0 1 .4 1 1 0 1.3.2 2.5.6 3.6.1.3 0 .7-.2 1z"/></svg>
        212-555-0147
      </li>
      <li>
        <svg viewBox="0 0 24 24" aria-hidden="true"><path d="M7 2h10a2 2 0 0 1 2 2v16a2 2 0 0 1-2 2H7a2 2 0 0 1-2-2V4a2 2 0 0 1 2-2zm0 3v12h10V5zm5 13.5a1.2 1.2 0 1 0 0 2.4 1.2 1.2 0 0 0 0-2.4z"/></svg>
        212-555-0147
      </li>
      <li>
        <svg viewBox="0 0 24 24" aria-hidden="true"><path d="M7 2h8l3 3v5h2a2 2 0 0 1 2 2v8a2 2 0 0 1-2 2H4a2 2 0 0 1-2-2v-8a2 2 0 0 1 2-2h3zm2 2v6h7V6h-2V4zM6 14v2h3v-2zm5 0v2h3v-2zm5 0v2h3v-2z"/></svg>
        212-555-0147
      </li>
      <li>
        <svg viewBox="0 0 24 24" aria-hidden="true"><path d="M12 2a10 10 0 1 0 5 18.7l-1-1.7A8 8 0 1 1 20 12v1.2c0 1-.7 1.8-1.5 1.8S17 14.2 17 13.2V7h-2v1a5 5 0 1 0 .8 7.1A3.4 3.4 0 0 0 18.5 17c2 0 3.5-1.7 3.5-3.8V12A10 10 0 0 0 12 2zm0 13a3 3 0 1 1 0-6 3 3 0 0 1 0 6z"/></svg>
        jun.pa@lanviretnode.com
      </li>
      <li>
        <svg viewBox="0 0 24 24" aria-hidden="true"><path d="M12 2a10 10 0 1 0 0 20 10 10 0 0 0 0-20zm6.9 6h-3a15 15 0 0 0-1.3-3.8A8 8 0 0 1 18.9 8zM12 4a13 13 0 0 1 1.9 4h-3.8A13 13 0 0 1 12 4zM4.3 14a8 8 0 0 1 0-4h3.4a16 16 0 0 0 0 4zm.8 2h3a15 15 0 0 0 1.3 3.8A8 8 0 0 1 5.1 16zM8.1 8h-3a8 8 0 0 1 4.3-3.8A15 15 0 0 0 8.1 8zM12 20a13 13 0 0 1-1.9-4h3.8A13 13 0 0 1 12 20zm2.3-6H9.7a14 14 0 0 1 0-4h4.6a14 14 0 0 1 0 4zm.3 5.8a15 15 0 0 0 1.3-3.8h3a8 8 0 0 1-4.3 3.8zm1.7-5.8a16 16 0 0 0 0-4h3.4a8 8 0 0 1 0 4z"/></svg>
        www.lanviretnode.com
      </li>
    </ul>
    <div class="brand">LVNODE</div>
  </div>
</body>
</html>
```